Opening a Hair Salon

Looking for a design for my sign that looks high end, an emphasis on color but welcoming to men and women.

The name is Kelvane Haircuts and Colors

Trying capture a more affluent client. Looking for a very modern look.

Reason: Time is going to quick and would like to see a few more options.

```html
<!DOCTYPE html>
<html lang="en">
<head>
<meta charset="utf-8">
<title>Kelvane Haircuts and Colors – Sign</title>
<link rel="stylesheet" href="https://fonts.googleapis.com/css2?family=Cormorant+Garamond:wght@500&family=Share+Tech+Mono&family=Didact+Gothic&display=swap">
<style>
  :root {
    --sign-black: #000000;
    --ink-white: #ffffff;
    --salon-green: #5fc21c;
  }
  html, body {
    margin: 0;
    padding: 0;
    overflow: hidden;
    background: var(--sign-black);
  }
  .sign {
    position: relative;
    width: 1200px;
    height: 360px;
    background: var(--sign-black);
    overflow: hidden;
  }
  .sign__name {
    position: absolute;
    left: 84px;
    top: 52px;
    margin: 0;
    font-family: "Cormorant Garamond", "Times New Roman", serif;
    font-weight: 500;
    font-size: 112px;
    line-height: 1;
    letter-spacing: 6px;
    color: var(--ink-white);
  }
  .sign__tagline {
    position: absolute;
    left: 266px;
    top: 201px;
    margin: 0;
    font-family: "Share Tech Mono", "Courier New", monospace;
    font-size: 35px;
    line-height: 1;
    letter-spacing: 8.2px;
    color: var(--salon-green);
  }
  .sign__rule {
    position: absolute;
    left: 42px;
    top: 268px;
    width: 1122px;
    height: 1.5px;
    background: var(--ink-white);
  }
  .sign__contact {
    position: absolute;
    right: 34px;
    top: 280px;
    display: flex;
    align-items: baseline;
    gap: 14px;
    margin: 0;
    white-space: nowrap;
  }
  .contact__web {
    font-family: "Share Tech Mono", "Courier New", monospace;
    font-size: 17px;
    letter-spacing: 3.4px;
    color: var(--salon-green);
  }
  .contact__phone {
    font-family: "Didact Gothic", "Trebuchet MS", sans-serif;
    font-size: 26px;
    letter-spacing: 2.6px;
    color: var(--ink-white);
  }
  .contact__dot {
    display: inline-block;
    width: 6px;
    height: 6px;
    border-radius: 50%;
    background: var(--ink-white);
    align-self: center;
    margin-top: 6px;
  }
</style>
</head>
<body>
  <main class="sign">
    <h1 class="sign__name">KELVANE</h1>
    <p class="sign__tagline">HAIRCUTS AND COLORS</p>
    <div class="sign__rule"></div>
    <p class="sign__contact">
      <span class="contact__web">www.kelvanehairsalon.com</span>
      <span class="contact__dot" aria-hidden="true"></span>
      <span class="contact__phone">952 555 184</span>
      <span class="contact__dot" aria-hidden="true"></span>
      <span class="contact__phone">670 555 302</span>
    </p>
  </main>
</body>
</html>
```